Urgent - brand new business card for a startup technical advisory and incubation business in Sydney

We need a brand new business card design for BrightForge. We are a startup technical advisory and incubation business based in Sydney Australia. We work with entrepreneurs and innovators to help rapidly and efficiently turn their ideas into reality and to ensure they have the technical platform required for growth.

Our name is partly inspired by our love of lean product development methods and the lean startup movement.

We would like clean, uncluttered designs that feature our two logo colours and communicate a professional but creative, in-touch and entrepreneurial business.

PLEASE SEE MUST HAVE PRIORITIES FOR DRAFT CONTACT INFORMATION AND OTHER DESIRED TEXT ON CARD.
Updates

We have now updated the brief to include draft business card contact information and also some additional desired text to feature on the card design.    Please review the Must Have priorities.

Also final updated source files for the horizontal and vertical versions have now been uploaded and should be used for any designs.

Thanks!

Target Market(s)

Entrepeneurs, innovators, startup investors looking for a strong product development partner

Industry/Entity Type

Business

Requirements
Must have
• Feature our two logo colours
Be a relatively clean, pared back overall design - quite minimalist

Updated source files (AI) for vertical and horizontal layouts attached.

Draft contact information for business card:
Neil Barton
Founder & CTO
Phone: +61 427 555123
Email: xxxx@brightforge.com
Skype: xxxxxbarton
Twitter: nbarton

www.brightforge.com

We would also like the overall design to include the phrase "You have great ideas. Let us make them happen." (probably in a reasonably subtle way)

Nice to have
• Inspire me! Double-sided designs are fine with logo, phrase, (URL?) on one side and contact details on other (+ any other design elements)

Logo on business card can be either with lightbulb above the wording as per example here or to the left of the BrightForge wording - both layouts in files provided.
Should not have
• Shouldn't look like a Pentara Suite business card template :-)

```html
<!DOCTYPE html>
<html lang="en">
<head>
<meta charset="utf-8">
<title>BrightForge – Business Card</title>
<link rel="stylesheet" href="https://fonts.googleapis.com/css2?family=Lato:wght@400;700&display=swap">
<style>
  :root {
    --stage: #4a4c50;
    --brand-blue: #2aa9de;
    --brand-ink: #3a3e44;
    --card-white: #ffffff;
    --text-grey: #55595f;
    --rule: #6b6f75;
    --tagline: #e8f6fc;
  }
  * { margin: 0; padding: 0; box-sizing: border-box; }
  html, body {
    width: 1200px; height: 900px; overflow: hidden;
    background: var(--stage);
    font-family: "Lato", sans-serif;
  }
  .sheet {
    width: 1200px; height: 900px;
    display: flex; flex-direction: column; align-items: center; justify-content: center;
    gap: 30px;
  }
  .card {
    width: 700px; height: 400px; position: relative;
    box-shadow: 0 6px 18px rgba(0,0,0,0.35);
  }

  /* Front */
  .card--front { background: var(--brand-blue); }
  .front__tagline {
    position: absolute; top: 38px; right: 40px;
    font-size: 15px; color: var(--tagline); letter-spacing: 0.2px;
  }
  .front__logo {
    position: absolute; top: 120px; left: 70px;
    display: flex; align-items: center; gap: 34px;
  }
  .front__mark {
    width: 130px; height: 130px; border-radius: 50%;
    background: var(--card-white); opacity: 0.9;
  }
  .front__name {
    font-weight: 700; font-size: 78px; color: var(--brand-ink); letter-spacing: -1px;
  }
  .front__url {
    position: absolute; bottom: 62px; left: 270px;
    font-size: 17px; letter-spacing: 6px; color: var(--brand-ink); text-transform: uppercase;
  }

  /* Back */
  .card--back { background: var(--card-white); display: flex; align-items: center; }
  .back__logo {
    width: 320px; display: flex; flex-direction: column; align-items: center; gap: 14px;
  }
  .back__mark {
    width: 96px; height: 96px; border-radius: 50%; background: var(--brand-blue);
  }
  .back__name {
    font-weight: 700; font-size: 46px; color: var(--brand-blue); letter-spacing: -0.5px;
  }
  .back__divider {
    width: 1px; height: 150px; background: var(--rule);
  }
  .back__details { padding-left: 44px; }
  .person__name {
    font-size: 22px; color: var(--brand-blue); text-transform: uppercase; letter-spacing: 0.5px;
  }
  .person__role { font-size: 18px; color: var(--text-grey); margin-top: 2px; }
  .contact { list-style: none; margin-top: 26px; }
  .contact__item {
    display: flex; align-items: center; gap: 10px;
    font-size: 17px; color: var(--text-grey); line-height: 28px;
  }
  .contact__icon { width: 14px; height: 14px; flex: none; }
</style>
</head>
<body>
<main class="sheet">
  <section class="card card--front" aria-label="Card front">
    <p class="front__tagline">You have great ideas. Let us make them happen.</p>
    <div class="front__logo">
      <div class="front__mark" aria-hidden="true"></div>
      <span class="front__name">BrightForge</span>
    </div>
    <p class="front__url">www.brightforge.com</p>
  </section>

  <section class="card card--back" aria-label="Card back">
    <div class="back__logo">
      <div class="back__mark" aria-hidden="true"></div>
      <span class="back__name">BrightForge</span>
    </div>
    <div class="back__divider" aria-hidden="true"></div>
    <div class="back__details">
      <p class="person__name">Neil Barton</p>
      <p class="person__role">Founder &amp; CTO</p>
      <ul class="contact">
        <li class="contact__item">
          <svg class="contact__icon" viewBox="0 0 14 14" aria-hidden="true">
            <circle cx="7" cy="7" r="6.5" fill="none" stroke="#2aa9de" stroke-width="1"/>
            <path d="M4.5 3.8 l1.2 0 l0.6 1.6 l-0.8 0.6 q0.6 1.4 2 2 l0.6 -0.8 l1.6 0.6 l0 1.2 q-3.8 0.4 -5.2 -5.2z" fill="#2aa9de"/>
          </svg>
          +61 427 555123
        </li>
        <li class="contact__item">
          <svg class="contact__icon" viewBox="0 0 14 14" aria-hidden="true">
            <rect x="1" y="3" width="12" height="8.5" rx="1" fill="#2aa9de"/>
            <path d="M1.5 3.6 L7 8 L12.5 3.6" fill="none" stroke="#fff" stroke-width="1"/>
          </svg>
          xxxx@brightforge.com
        </li>
        <li class="contact__item">
          <svg class="contact__icon" viewBox="0 0 14 14" aria-hidden="true">
            <circle cx="7" cy="7" r="6.5" fill="#2aa9de"/>
          </svg>
          xxxxxbarton
        </li>
        <li class="contact__item">
          <svg class="contact__icon" viewBox="0 0 14 14" aria-hidden="true">
            <rect x="0.5" y="0.5" width="13" height="13" rx="2" fill="#2aa9de"/>
          </svg>
          nbarton
        </li>
      </ul>
    </div>
  </section>
</main>
</body>
</html>
```